Vortapallo Rindelmo needs your help to create a new identity design

We are a basketball team based in Crescentino, Italy.
The official club colors are royal blue and white.
Basically we need a new letterhead and envelope design but not necessary a new logo, but if you want to suggest us a new one we are glad to evaluate it.
If you need any other info please contact us.

Target Market(s)

athletes, their families, other clubs, public institutions, companies

Industry/Entity Type

Club

Other font styles liked:
• the font of our logo or something very similar

Colors
0592cd
ffffff

Requirements
Must have
• our logo, attached to this request; address and other club info such as email address, phone number, facebook page, VAT lot and tax code and obviously our official club colors royal blue and white
Nice to have
• a clear, simple and quite minimal design. A watermark
Should not have
• any other graphic or images such as hoops, ball or court

```html
<!DOCTYPE html>
<html lang="en">
<head>
<meta charset="utf-8">
<title>Vortapallo Rindelmo – Letterhead and Envelope</title>
<link href="https://fonts.googleapis.com/css2?family=Open+Sans:wght@400;700&family=Great+Vibes&display=swap" rel="stylesheet">
<style>
  :root{
    --club-blue:#1591cf;
    --club-navy:#1f2d5c;
    --paper:#ffffff;
    --ink:#3d3d3d;
    --watermark:#ececec;
    --rule:#bfe0f1;
    --stage:#2e2e2e;
  }
  *{margin:0;padding:0;box-sizing:border-box}
  html,body{width:1200px;height:1200px;overflow:hidden}
  body{background:var(--stage);font-family:"Open Sans",sans-serif;position:relative}

  .letterhead{position:absolute;left:30px;top:211px;width:600px;height:777px;background:var(--paper);overflow:hidden}
  .envelope{position:absolute;left:660px;top:211px;width:510px;height:221px;background:var(--paper);overflow:hidden}

  .club-mark{position:absolute;display:flex;align-items:center;gap:7px;color:var(--club-navy);font-weight:700;white-space:nowrap}
  .club-mark .dot{border-radius:50%;background:var(--club-navy);flex:none}
  .letterhead .club-mark{left:0;right:0;top:48px;justify-content:center;font-size:17px}
  .letterhead .club-mark .dot{width:16px;height:16px}
  .envelope .club-mark{left:26px;top:46px;font-size:12px}
  .envelope .club-mark .dot{width:12px;height:12px}

  .watermark{position:absolute;border-radius:50%;background:radial-gradient(circle,var(--watermark) 0%,#f3f3f3 70%,rgba(255,255,255,0) 100%)}
  .letterhead .watermark{left:270px;top:520px;width:340px;height:340px}
  .envelope .watermark{left:300px;top:20px;width:240px;height:240px}

  .letter-body{position:absolute;left:44px;top:170px;color:var(--ink);font-size:10.6px;line-height:24px;white-space:nowrap}
  .recipient{margin-bottom:24px}
  .paragraph{margin-bottom:24px}
  .closing{position:absolute;left:44px;top:533px;color:var(--ink)}
  .closing .thanks{font-size:15.5px;line-height:20px}
  .closing .signature{font-family:"Great Vibes",cursive;color:var(--club-blue);font-size:36px;line-height:38px}

  .contact-rule{position:absolute;height:1px;background:var(--rule)}
  .contact-line{position:absolute;display:flex;align-items:center;color:var(--club-blue);white-space:nowrap}
  .contact-line .item{display:flex;align-items:center;gap:2px}
  .contact-line svg{fill:var(--club-blue);flex:none}
  .blue-band{position:absolute;left:0;right:0;bottom:0;background:var(--club-blue)}

  .letterhead .contact-rule{left:10px;right:10px;top:736px}
  .letterhead .contact-line{left:10px;top:741px;font-size:7.4px;gap:6px}
  .letterhead .contact-line svg{width:7px;height:7px}
  .letterhead .blue-band{height:19px}

  .envelope .contact-rule{left:11px;right:43px;top:182px}
  .envelope .contact-line{left:12px;top:188px;font-size:6.1px;gap:4.5px}
  .envelope .contact-line svg{width:6px;height:6px}
  .envelope .blue-band{height:18px}
</style>
</head>
<body>

<section class="letterhead">
  <div class="watermark" role="img" aria-label="Faint club emblem watermark"></div>
  <div class="club-mark"><span class="dot"></span>Vortapallo Rindelmo</div>

  <div class="letter-body">
    <div class="recipient">To<br>The,<br>Director</div>
    <p class="paragraph">Lorem ipsum dolor sit amet, consectetur adipiscing elit. Integer nec odio, sed<br>
    dictum, massa quam dapibus leo, eget vulputate nibh lorem ac turpis. Donec<br>
    aliquam quam vel dolor. Nunc adipiscing. Sed lacinia, urna non tincidunt.<br>
    Vestibulum ut nulla aliquam risus rutrum interdum.</p>
    <p class="paragraph">Curabitur sit amet&nbsp; erat quis risus feugiat viverra. Pellentesque augue justo,<br>
    non, arcu.&nbsp; Nunc nec libero. In cursus dictum justo, vel tempor dui sagittis<br>
    dolonunc,egestas at, accumsan at, malesuada id, nisl. Orci varius natoque<br>
    ipsum primis in faucibus orci luctus et ultrices posuere cubilia curae; donec<br>
    vehicula. Nullam quis enim. Integer dignissim viverra velit.</p>
  </div>

  <div class="closing">
    <div class="thanks">Thanking you</div>
    <div class="signature">John Doe</div>
  </div>

  <div class="contact-rule"></div>
  <div class="contact-line">
    <span class="item"><svg viewBox="0 0 10 10"><path d="M1 3c0-1 2-2 4-2s4 1 4 2v1H7V3H3v1H1zM2 5h6l1 4H1z"/></svg>123-456-7890</span>
    <span class="item"><svg viewBox="0 0 10 10"><path d="M5 0a5 5 0 1 0 0 10A5 5 0 0 0 5 0zm0 1c.6 0 1.2 1.5 1.3 3.5H3.7C3.8 2.5 4.4 1 5 1zM1.1 5.5h1.6c.1 1.4.4 2.6.8 3.2A4 4 0 0 1 1.1 5.5zm0-1A4 4 0 0 1 3.5 1.3c-.4.6-.7 1.8-.8 3.2zm2.6 1h2.6C6.2 7.5 5.6 9 5 9s-1.2-1.5-1.3-3.5zm3.6 0h1.6a4 4 0 0 1-2.4 3.2c.4-.6.7-1.8.8-3.2zm0-1c-.1-1.4-.4-2.6-.8-3.2a4 4 0 0 1 2.4 3.2z"/></svg>www.vortapallorindelmo.com</span>
    <span class="item"><svg viewBox="0 0 10 10"><rect x="0" y="1.5" width="10" height="7"/></svg>john@vortapallorindelmo.com</span>
    <span class="item"><svg viewBox="0 0 10 10"><rect x="0.5" y="0.5" width="9" height="9"/></svg>vortapallorindelmo</span>
    <span class="item"><svg viewBox="0 0 10 10"><path d="M5 0l1.2 3.6H10L7 5.9 8.1 9.5 5 7.3 1.9 9.5 3 5.9 0 3.6h3.8z"/></svg>VAT : xxxxxxxx xx</span>
    <span class="item"><svg viewBox="0 0 10 10"><path d="M5 0l1.2 3.6H10L7 5.9 8.1 9.5 5 7.3 1.9 9.5 3 5.9 0 3.6h3.8z"/></svg>Tax Code : xxxxxxxxxx</span>
  </div>
  <div class="blue-band"></div>
</section>

<section class="envelope">
  <div class="watermark" role="img" aria-label="Faint club emblem watermark"></div>
  <div class="club-mark"><span class="dot"></span>Vortapallo Rindelmo</div>

  <div class="contact-rule"></div>
  <div class="contact-line">
    <span class="item"><svg viewBox="0 0 10 10"><path d="M1 3c0-1 2-2 4-2s4 1 4 2v1H7V3H3v1H1zM2 5h6l1 4H1z"/></svg>123-456-7890</span>
    <span class="item"><svg viewBox="0 0 10 10"><path d="M5 0a5 5 0 1 0 0 10A5 5 0 0 0 5 0zm0 1c.6 0 1.2 1.5 1.3 3.5H3.7C3.8 2.5 4.4 1 5 1zM1.1 5.5h1.6c.1 1.4.4 2.6.8 3.2A4 4 0 0 1 1.1 5.5zm0-1A4 4 0 0 1 3.5 1.3c-.4.6-.7 1.8-.8 3.2zm2.6 1h2.6C6.2 7.5 5.6 9 5 9s-1.2-1.5-1.3-3.5zm3.6 0h1.6a4 4 0 0 1-2.4 3.2c.4-.6.7-1.8.8-3.2zm0-1c-.1-1.4-.4-2.6-.8-3.2a4 4 0 0 1 2.4 3.2z"/></svg>www.vortapallorindelmo.com</span>
    <span class="item"><svg viewBox="0 0 10 10"><rect x="0" y="1.5" width="10" height="7"/></svg>john@vortapallorindelmo.com</span>
    <span class="item"><svg viewBox="0 0 10 10"><rect x="0.5" y="0.5" width="9" height="9"/></svg>vortapallorindelmo</span>
    <span class="item"><svg viewBox="0 0 10 10"><path d="M5 0l1.2 3.6H10L7 5.9 8.1 9.5 5 7.3 1.9 9.5 3 5.9 0 3.6h3.8z"/></svg>VAT : xxxxxxxx xx</span>
    <span class="item"><svg viewBox="0 0 10 10"><path d="M5 0l1.2 3.6H10L7 5.9 8.1 9.5 5 7.3 1.9 9.5 3 5.9 0 3.6h3.8z"/></svg>Tax Code : xxxxxxxxxx</span>
  </div>
  <div class="blue-band"></div>
</section>

</body>
</html>
```